Portada libro no ficción: Rutas de empresa hacia lo Intangible

Busco diseño para libro de no ficción sobre los modelos de negocio del metaverso.

Maquetación de:
- Portada
- Contraportada
- Lomo

Requerimientos:
- Una portada única y creativa
- Portada para formato Lectoria, Vendalis y físico.
- Imágenes para el sitio web y las redes sociales
- Gráficos profesionales de alta calidad
- Adjuntar archivo de edición

Target:
- CEO
- CMO
- Emprendedor
- Gente relacionada con el marketing digital

Ideas iniciales de la portada:
- Minimalista
- Atemporal: Evitar gafas de realidad virtual (son productos que cambian con frecuencia)

Descripción del libro:
No se trata de un libro técnico sobre el metaverso. El objetivo del libro es llegar a marketers, CEOs, emprendedores, perfiles tecnológicos con visión de negocio que quieren descubrir cómo llevar su negocio o su idea de negocio al metaverso, y cómo aplicar modelos de negocio.

El libro se divide en un primer bloque de presentación del metaverso, introducción a la economía digital, y modelos de negocio aplicados al metaverso.

Ejemplos de portada:
- cover1: este formato es mi favorito, minimalista, atemporal y fácil de leer.
- cover2: esta portada me parece interesante por la cercanía con los colores habituales del metaverso.
- cover3: aunque con un toque retro (no es lo que busco), es un formato que me parece interesante por no recurrir a las gafas, y sin entrar en formato fotografía.
- cover4 y cover5: me gusta la relación de colores entre la letra y el fondo para dar prioridad al título.
- cover6: me gusta usar dos colores, en este caso para destacar metaverso, y la imagen de la portada te hace sentir más listo (por pensar diferente).

Título: "Rutas de empresa hacia lo intangible"

Texto asociado:
"Lidera la transición de tu negocio hacia el metaverso"

"Descubre los principales modelos de negocio del metaverso y cómo aplicarlos"

Autor: Tomàs Velabrun

```html
<!DOCTYPE html>
<html lang="es">
<head>
<meta charset="utf-8">
<title>Rutas de empresa hacia lo Intangible — Portada</title>
<link rel="stylesheet" href="https://fonts.googleapis.com/css2?family=Oswald:wght@300;400;500&display=swap">
<style>
  :root {
    --stage: #f1f2f4;
    --navy: #0b1a44;
    --band: rgba(22, 52, 122, 0.85);
    --sky-top: #16305f;
    --sky-cloud: #3b6496;
    --horizon-warm: #f2c9a0;
    --city-deep: #12295a;
    --city-amber: #ff9a4a;
    --city-glow: #6fd2ff;
    --floor-light: #bfeeff;
    --floor-deep: #0c2454;
    --ink: #ffffff;
    --ink-soft: #e6eefb;
  }
  * { box-sizing: border-box; margin: 0; padding: 0; }
  html, body {
    width: 1200px; height: 1187px; overflow: hidden;
    background: var(--stage);
  }
  .book-cover {
    position: absolute;
    left: 246px; top: 53px;
    width: 707px; height: 1080px;
    overflow: hidden;
    font-family: "Oswald", sans-serif;
    color: var(--ink);
    text-align: center;
    box-shadow: 0 6px 18px rgba(0,0,0,0.18);
  }
  .cover-art {
    position: absolute; inset: 0;
    background:
      radial-gradient(ellipse 60% 10% at 50% 84%, rgba(210,245,255,0.85), rgba(210,245,255,0) 70%),
      radial-gradient(ellipse 90% 22% at 50% 82%, rgba(111,210,255,0.8), rgba(111,210,255,0) 72%),
      radial-gradient(ellipse 18% 10% at 14% 56%, rgba(255,154,74,0.55), rgba(255,154,74,0) 70%),
      radial-gradient(ellipse 16% 9% at 82% 58%, rgba(255,154,74,0.5), rgba(255,154,74,0) 70%),
      radial-gradient(ellipse 14% 8% at 60% 45%, rgba(255,236,200,0.6), rgba(255,236,200,0) 70%),
      radial-gradient(ellipse 55% 12% at 50% 44%, rgba(242,201,160,0.45), rgba(242,201,160,0) 70%),
      radial-gradient(ellipse 120% 60% at 50% 110%, rgba(12,36,84,0) 55%, rgba(12,36,84,0.75) 100%),
      linear-gradient(180deg,
        var(--sky-top) 0%,
        var(--sky-cloud) 28%,
        #5d86b4 40%,
        #3a6aa4 47%,
        var(--city-deep) 55%,
        #1b3f7c 66%,
        #2f82c4 74%,
        #4bb4e6 82%,
        #2a6fb0 90%,
        var(--floor-deep) 100%);
  }
  .top-strip {
    position: absolute; left: 0; top: 0; width: 100%; height: 30px;
    background: var(--navy);
  }
  .tagline-band {
    position: absolute; left: 0; top: 30px; width: 100%; height: 48px;
    background: var(--band);
    display: flex; align-items: center; justify-content: center;
  }
  .tagline {
    font-weight: 500; font-size: 17px; letter-spacing: 1.6px;
    text-transform: uppercase;
  }
  .title {
    position: absolute; left: 0; top: 96px; width: 100%;
    font-weight: 400;
  }
  .title-lead {
    display: block;
    font-size: 54px; line-height: 1.05;
  }
  .title-key {
    display: block;
    font-size: 138px; line-height: 1.02;
    text-transform: uppercase; letter-spacing: -1px;
  }
  .subtitle {
    position: absolute; left: 0; right: 0; top: 340px;
    font-weight: 400; font-size: 20px; line-height: 1.35;
    text-transform: uppercase; color: var(--ink-soft);
    letter-spacing: 0.4px;
  }
  .subtitle span { display: block; }
  .author-band {
    position: absolute; left: 0; bottom: 0; width: 100%; height: 80px;
    background: var(--navy);
    display: flex; align-items: center; justify-content: center;
  }
  .author {
    font-weight: 400; font-size: 34px; letter-spacing: 2px;
    text-transform: uppercase;
  }
</style>
</head>
<body>
  <main class="book-cover">
    <div class="cover-art" role="img" aria-label="Fotografía: hombre de traje de espaldas frente a una ciudad nocturna iluminada, con una red de líneas de luz y una plataforma digital brillante"></div>
    <div class="top-strip"></div>
    <div class="tagline-band">
      <p class="tagline">'Lidera la transición de tu negocio hacia el metaverso'</p>
    </div>
    <h1 class="title">
      <span class="title-lead">Rutas de empresa hacia lo</span>
      <span class="title-key">Intangible</span>
    </h1>
    <p class="subtitle"><span>"Descubre los principales modelos de negocio del</span><span>metaverso y cómo aplicarlos"</span></p>
    <div class="author-band">
      <p class="author">Tomàs Velabrun</p>
    </div>
  </main>
</body>
</html>
```